Tamworth Logistics

Create a modern, simple, Elegant business card design for my business.

Services: Vexa Trucks, Transport, Contract Logistics,

Business

Include all details same as old card plus new website address: www.tamworthlogistics-demo.com.au

• Similar colors to Logo.

```html
<!DOCTYPE html>
<html lang="en">
<head>
<meta charset="utf-8">
<title>Tamworth Logistics – Business Card</title>
<link rel="stylesheet" href="https://fonts.googleapis.com/css2?family=Cabin:wght@400;600&display=swap">
<style>
  :root {
    --backdrop: #869996;
    --card-light: #e8eeec;
    --ink-black: #181b1c;
    --ink-charcoal: #2c3335;
    --ink-slate: #3b4446;
    --blue-deep: #2388ee;
    --blue-sky: #3fc5f7;
    --text-grey: #4a5356;
    --wordmark: #5d6668;
    --white: #ffffff;
  }
  * { box-sizing: border-box; margin: 0; padding: 0; }
  html, body { width: 1200px; height: 1200px; overflow: hidden; }
  body {
    background: var(--backdrop);
    font-family: "Cabin", sans-serif;
    position: relative;
  }
  .card {
    position: absolute;
    left: 244px;
    width: 666px;
    height: 380px;
    background: var(--card-light);
    overflow: hidden;
  }
  .card--front { top: 146px; }
  .card--back { top: 636px; }

  .edge-art {
    position: absolute;
    top: 0;
    height: 100%;
    background: linear-gradient(180deg, var(--ink-charcoal) 0%, var(--ink-black) 100%);
  }
  .card--front .edge-art--left { left: 0; width: 105px; }
  .card--front .edge-art--right { right: 0; width: 101px; }
  .card--back .edge-art--left { left: 0; width: 55px; }

  .contact-panel {
    position: absolute;
    left: 333px;
    top: 0;
    width: 333px;
    height: 100%;
    background: var(--ink-charcoal);
  }

  .brand {
    position: absolute;
    display: flex;
    align-items: center;
    gap: 10px;
    color: var(--wordmark);
    font-weight: 600;
    white-space: nowrap;
  }
  .brand__square { background: var(--blue-deep); flex: none; }
  .card--front .brand { left: 160px; top: 168px; font-size: 36px; }
  .card--front .brand__square { width: 26px; height: 26px; }
  .card--back .brand { left: 76px; top: 172px; font-size: 26px; gap: 8px; }
  .card--back .brand__square { width: 18px; height: 18px; }

  .services {
    position: absolute;
    left: 146px;
    top: 253px;
    display: flex;
    align-items: center;
    gap: 18px;
    font-size: 17px;
    color: var(--text-grey);
  }
  .services__divider { width: 3px; height: 11px; background: var(--blue-deep); }

  .contact {
    position: absolute;
    left: 333px;
    width: 333px;
    height: 44px;
    background: var(--blue-deep);
    color: var(--white);
  }
  .contact--name { top: 30px; }
  .contact--phone { top: 120px; }
  .contact--email { top: 209px; }
  .contact--web { top: 300px; }
  .contact__icon {
    position: absolute;
    left: 10px;
    top: 7px;
    width: 30px;
    height: 30px;
  }
  .contact__text {
    position: absolute;
    left: 48px;
    right: 4px;
    top: 0;
    height: 100%;
    display: flex;
    flex-direction: column;
    align-items: center;
    justify-content: center;
    text-align: center;
    white-space: nowrap;
  }
  .contact__name { font-size: 21px; font-weight: 600; line-height: 1.05; }
  .contact__role { font-size: 15px; line-height: 1.1; }
  .contact--phone .contact__text { font-size: 20px; font-weight: 600; }
  .contact--email .contact__text,
  .contact--web .contact__text { font-size: 15.5px; }
</style>
</head>
<body>

<section class="card card--front" aria-label="Business card front">
  <div class="edge-art edge-art--left" role="img" aria-label="Dark decorative edge band with blue folded ribbon accents"></div>
  <div class="edge-art edge-art--right" role="img" aria-label="Dark decorative edge band with blue frame accent"></div>

  <div class="brand"><span class="brand__square"></span>Tamworth Logistics</div>

  <div class="services">
    <span>Vexa Trucks</span>
    <span class="services__divider"></span>
    <span>Transport</span>
    <span class="services__divider"></span>
    <span>Contract Logistics</span>
  </div>
</section>

<section class="card card--back" aria-label="Business card back">
  <div class="edge-art edge-art--left" role="img" aria-label="Dark decorative edge band with blue folded ribbon accents"></div>
  <div class="contact-panel"></div>

  <div class="brand"><span class="brand__square"></span>Tamworth Logistics</div>

  <div class="contact contact--name">
    <svg class="contact__icon" viewBox="0 0 30 30" aria-hidden="true">
      <circle cx="15" cy="15" r="14" fill="var(--ink-slate)"/>
      <circle cx="15" cy="11" r="4.5" fill="var(--blue-sky)"/>
      <path d="M7,23 a8,7 0 0 1 16,0 z" fill="var(--blue-sky)"/>
    </svg>
    <div class="contact__text">
      <span class="contact__name">Individual Name</span>
      <span class="contact__role">Position</span>
    </div>
  </div>

  <div class="contact contact--phone">
    <svg class="contact__icon" viewBox="0 0 30 30" aria-hidden="true">
      <path d="M6,6 l5,-2 l4,7 l-3,3 q2,5 7,8 l3,-3 l7,4 l-2,5 q-9,2 -17,-7 q-6,-8 -4,-15 z" fill="var(--ink-slate)"/>
    </svg>
    <div class="contact__text">0400 555 123</div>
  </div>

  <div class="contact contact--email">
    <svg class="contact__icon" viewBox="0 0 30 30" aria-hidden="true" fill="none" stroke="var(--ink-slate)" stroke-width="1.3">
      <circle cx="15" cy="15" r="13"/>
      <ellipse cx="15" cy="15" rx="6" ry="13"/>
      <path d="M2,15 h26 M4,8 h22 M4,22 h22 M15,2 v26"/>
    </svg>
    <div class="contact__text">Demo@tamworthlogistics-demo.com.au</div>
  </div>

  <div class="contact contact--web">
    <svg class="contact__icon" viewBox="0 0 30 30" aria-hidden="true" fill="none" stroke="var(--ink-slate)" stroke-width="1.3">
      <circle cx="15" cy="15" r="13"/>
      <ellipse cx="15" cy="15" rx="6" ry="13"/>
      <path d="M2,15 h26 M4,8 h22 M4,22 h22 M15,2 v26"/>
    </svg>
    <div class="contact__text">www.tamworthlogistics-demo.com.au</div>
  </div>
</section>

</body>
</html>
```